TRV Conference Newsletter Postcard

We need a template design for a direct mailer postcard that we are sending to potential attendees. The attached templates include the dimensions of the postcard. It is a panel/map type of postcard so it has 8 surfaces that need to have content on them. The purpose of this project is to get people to sign up and attend our conference in May. I have attached what type of layout we would like to have on each panel of the postcard.

Target Market(s)

Category Managers, Shopper Insights, Shopper Marketing

Industry/Entity Type

Consumer

Font styles to use
Sans Serif

Requirements
Must have
• A fun but clean template that includes designs, graphics, elements that show lists, our agenda, pop up graphics that can show facts and stats.
• An interesting shopper cart graphic that include insights, analytics, data, networking, etc.
Nice to have
• Maybe some fun content based on the conference title.
Should not have
• No animated characters. We want this to be clean and innovative, but fun.

```html
<!DOCTYPE html>
<html lang="en">
<head>
<meta charset="utf-8">
<title>TRV Conference Mailer</title>
<link rel="stylesheet" href="https://fonts.googleapis.com/css2?family=Open+Sans:wght@400;600;700&family=Oswald:wght@600;700&display=swap">
<style>
  :root {
    --paper: #f2f2ef;
    --blue: #1f6fb4;
    --blue-deep: #0f4f8f;
    --blue-light: #3aa3d8;
    --gray: #b9bcc0;
    --ink: #2b2b2b;
    --teal: #2a9fd0;
    --map-a: #e8e9e4;
    --map-b: #dfe3dc;
  }
  * { box-sizing: border-box; margin: 0; padding: 0; }
  html, body { width: 1200px; height: 800px; overflow: hidden; background: var(--paper); }
  body { font-family: "Open Sans", Arial, sans-serif; color: var(--ink); position: relative; }

  .postcard { position: absolute; inset: 0; background: var(--paper); overflow: hidden; }
  .swooshes { position: absolute; inset: 0; width: 1200px; height: 800px; }

  .map-area {
    position: absolute; left: 640px; top: 300px; width: 560px; height: 500px;
    background: linear-gradient(160deg, var(--map-a), var(--map-b));
  }

  .day-header {
    position: absolute; display: flex; width: 190px; height: 38px;
    font-size: 11px; line-height: 1.15; color: #fff;
  }
  .day-header span { display: flex; align-items: center; padding: 0 10px; background: var(--blue); }
  .day-header .day { width: 88px; border-right: 2px solid var(--paper); }
  .day-header .track { flex: 1; }

  .agenda { position: absolute; list-style: none; font-size: 11px; line-height: 1.25; }
  .agenda li { margin-bottom: 8px; }
  .agenda .time { display: block; }
  .agenda .note { display: block; }

  .brand-mark {
    position: absolute; display: flex; align-items: center; gap: 8px;
    font-family: "Open Sans", Arial, sans-serif; font-weight: 700; color: var(--blue);
  }
  .brand-mark .box { width: 34px; height: 34px; background: var(--blue); }
  .brand-mark.small { font-size: 13px; }
  .brand-mark.small .box { width: 22px; height: 22px; }
  .brand-mark.large { font-size: 20px; }

  .banner {
    position: absolute; left: 680px; top: 40px; width: 460px; height: 190px;
    background: linear-gradient(120deg, var(--blue-deep), var(--blue) 55%, var(--blue-light));
    clip-path: polygon(6% 0, 100% 0, 100% 100%, 0 100%);
    color: #fff; font-family: "Oswald", Impact, sans-serif; text-transform: uppercase;
    padding: 26px 24px 0 66px; transform: skewY(5deg); transform-origin: left top;
  }
  .banner .line1, .banner .line2 { font-size: 40px; line-height: 1; font-weight: 700; }
  .banner .line3 { font-size: 22px; line-height: 1.2; font-weight: 600; margin-top: 4px; }

  .mail-label { position: absolute; left: 700px; top: 292px; font-size: 15px; }
  .stamp-label { position: absolute; left: 1100px; top: 325px; font-size: 20px; }

  .contact {
    position: absolute; left: 455px; top: 632px; width: 250px;
    font-size: 11px; line-height: 1.6; font-style: normal;
  }
  .contact .web { color: var(--teal); }
</style>
</head>
<body>
<main class="postcard">

  <div class="map-area" role="img" aria-label="Faint street map of the conference city"></div>

  <svg class="swooshes" viewBox="0 0 1200 800" aria-hidden="true">
    <path d="M30 40 Q120 0 210 20" fill="none" stroke="var(--blue)" stroke-width="6"/>
    <path d="M40 48 Q130 10 220 30" fill="none" stroke="var(--gray)" stroke-width="4"/>
    <path d="M20 760 Q140 680 300 740" fill="none" stroke="var(--blue)" stroke-width="12"/>
    <path d="M30 772 Q150 700 310 760" fill="none" stroke="var(--gray)" stroke-width="6"/>
    <path d="M420 558 Q720 468 860 800" fill="none" stroke="var(--gray)" stroke-width="22"/>
    <path d="M420 540 Q720 450 880 800" fill="none" stroke="var(--blue)" stroke-width="12"/>
    <path d="M420 580 Q720 490 840 800" fill="none" stroke="var(--blue-light)" stroke-width="28"/>
    <path d="M660 255 Q880 310 1060 280" fill="none" stroke="var(--blue)" stroke-width="8"/>
    <path d="M660 271 Q880 326 1060 296" fill="none" stroke="var(--gray)" stroke-width="5"/>
  </svg>

  <div class="brand-mark small" style="left:320px; top:12px;"><span class="box"></span>TRV Conference</div>

  <div class="day-header" style="left:30px; top:45px;"><span class="day">Monday<br>5/15</span><span class="track">Main<br>Conference</span></div>
  <ul class="agenda" style="left:40px; top:95px; width:190px;">
    <li><span class="time">1:00 - 2:15 PM</span>Speed Networking</li>
    <li><span class="time">2:30 - 3:00 PM</span>Opening Welcome</li>
    <li><span class="time">3:00 - 3:30 PM</span>Keynote Speaker</li>
    <li><span class="time">3:30 - 4:00 PM</span>Keynote Speaker</li>
    <li><span class="time">4:00 - 4:20 PM</span>Break</li>
    <li><span class="time">4:20 - 5:05 PM</span>Breakout Sessions</li>
    <li><span class="time">5:15 - 6:15 PM</span>Solution Provider Demos<span class="note">3 rounds, 15 min rotations,<br>5 min in between</span></li>
    <li><span class="time">6:15 - 7:30 PM</span>Networking Reception<br>&amp; Hors d'oeuvres</li>
  </ul>

  <div class="day-header" style="left:30px; top:470px;"><span class="day">Tuesday<br>5/16</span><span class="track">Main<br>Conference</span></div>
  <ul class="agenda" style="left:40px; top:520px; width:190px;">
    <li><span class="time">7:00 - 8:30 AM</span>Networking Breakfast</li>
    <li><span class="time">8:30 - 8:45 AM</span>The Day's Highlights</li>
    <li><span class="time">8:45 - 9:30 AM</span>Keynote Speaker</li>
  </ul>

  <div class="day-header" style="left:250px; top:70px;"><span class="day">Tuesday<br>5/16</span><span class="track">Main<br>Conference</span></div>
  <ul class="agenda" style="left:262px; top:120px; width:190px;">
    <li><span class="time">9:30 - 10:00 AM</span>Keynote Speaker</li>
    <li><span class="time">10:00 - 10:20 AM</span>Break</li>
    <li><span class="time">10:20 - 10:50 AM</span>IP Presentations</li>
    <li><span class="time">11:00 - 11:45 AM</span>Breakout Sessions</li>
    <li><span class="time">11:45 - 1:00 PM</span>Networking Lunch</li>
    <li><span class="time">1:00 - 2:35 PM</span>Solution Provider Demos<span class="note">3 rounds, 15 min rotations,<br>5 min in between</span></li>
    <li><span class="time">2:45 - 3:30 PM</span>Breakout Sessions</li>
    <li><span class="time">3:40 - 4:10 PM</span>IP Presentations</li>
    <li><span class="time">4:10 - 4:30 PM</span>Break</li>
    <li><span class="time">4:30 - 5:15 PM</span>Keynote Speaker</li>
    <li><span class="time">5:15 - 6:30 PM</span>Networking Reception<br>&amp; Hors d'oeuvres</li>
    <li><span class="time">6:30 PM</span>Open Dinner</li>
    <li><span class="time">8:30 PM</span>Late Night Event</li>
  </ul>

  <div class="day-header" style="left:460px; top:100px;"><span class="day">Wednesday<br>5/17</span><span class="track">Main<br>Conference</span></div>
  <ul class="agenda" style="left:472px; top:150px; width:180px;">
    <li><span class="time">7:30 - 9:00 AM</span>Networking Breakfast</li>
    <li><span class="time">9:00 - 9:45 AM</span>Keynote Speaker</li>
    <li><span class="time">9:45 - 10:15 AM</span>Keynote Speaker</li>
    <li><span class="time">10:15 - 10:30 AM</span>Break</li>
    <li><span class="time">10:30 - 11:00 AM</span>IP Presentation</li>
    <li><span class="time">11:10 - 11:55 AM</span>Breakout Sessions</li>
    <li><span class="time">11:55 - 1:30 PM</span>Networking Lunch</li>
    <li><span class="time">1:30 - 3:30 PM</span>Case Study Workshops</li>
    <li><span class="time">3:30 - 4:15 PM</span>Keynote Speaker</li>
    <li><span class="time">4:15 - 4:30 PM</span>Closing Remarks</li>
  </ul>

  <header class="banner">
    <div class="line1">Category</div>
    <div class="line2">Management &amp;</div>
    <div class="line3">Shopper Insights Conference</div>
  </header>

  <p class="mail-label">Mailing Address Area</p>
  <p class="stamp-label">Stamp</p>

  <div class="brand-mark large" style="left:900px; top:440px;"><span class="box"></span>TRV Conference</div>

  <div class="brand-mark small" style="left:455px; top:600px;"><span class="box"></span>TRV Conference</div>
  <address class="contact">
    4820 Lakeview Parkway, Suite 300<br>
    Riverton, MN 55400<br>
    Phone: 612.555.0148<br>
    Email: members@trvnetwork.org<br>
    <span class="web">Web: trvconference.org</span>
  </address>

</main>
</body>
</html>
```